Cell Tower company needs website updated

We need a website that does not look like it was designed in the early 1990's. The company fabricates, installs and reinforces communication towers throughout the US, Caribbean, Central and S. America. We are located in Pensacola Florida. Our tower technicians travel to wherever the work is. I have some good pictures taken from towers to use on the site. I want the site to reflect the excitement that the wireless communication industry has. I want to the company to look exciting and attract new employees. The majority of our business is modifying and reinforcing existing cell towers to accept all the new tower top antennas that the increasing wireless mobile world demands.
Updates

I have added some sample photos from our business to our ArtBazaar profile.

We are now going through each design to find what is most suitable for our needs. Thank you all for your time in this matter.

Industry/Entity Type

Wireless Communication

```html
<!DOCTYPE html>
<html lang="en">
<head>
<meta charset="utf-8">
<title>SpanRidge Structures</title>
<link rel="stylesheet" href="https://fonts.googleapis.com/css2?family=Oswald:wght@400;500;600&family=Open+Sans:wght@400;600;700&display=swap">
<style>
:root{
  --red:#c81e1e;
  --red-dark:#9e1414;
  --ink:#333;
  --muted:#777;
  --line:#ddd;
  --grey-band:#ececec;
  --footer:#2b2b2b;
  --footer-bottom:#1d1d1d;
  --hero-a:#5a6e80;
  --hero-b:#1d2631;
  --white:#fff;
}
*{margin:0;padding:0;box-sizing:border-box}
html,body{width:713px;height:1200px;overflow:hidden;background:var(--white)}
body{font-family:"Open Sans",sans-serif;color:var(--ink);font-size:8px;line-height:1.45;position:relative}
.wrap{width:653px;margin:0 auto;position:relative}
h2,h3,h4,.nav a,.hero-title{font-family:"Oswald",sans-serif;font-weight:500;text-transform:uppercase}

/* header */
.site-header{height:62px;display:flex;align-items:center;justify-content:space-between}
.brand{display:flex;align-items:center;gap:7px;font-size:17px;font-weight:700;color:var(--red)}
.brand .dot{width:14px;height:14px;background:var(--red)}
.call{text-align:right;font-family:"Oswald",sans-serif}
.call small{display:block;font-size:8px;color:var(--muted);letter-spacing:1px}
.call strong{font-size:18px;color:var(--red);font-weight:500}

/* nav */
.nav{height:22px;background:var(--red);display:flex}
.nav a{color:var(--white);text-decoration:none;font-size:8.5px;padding:0 12px;line-height:22px;letter-spacing:.3px}
.nav a.active{background:var(--red-dark)}

/* hero */
.hero{height:336px;position:relative;background:linear-gradient(160deg,var(--hero-a),var(--hero-b))}
.arrow{position:absolute;top:150px;width:22px;height:30px;background:rgba(0,0,0,.45);display:flex;align-items:center;justify-content:center}
.arrow.left{left:0}.arrow.right{right:0}
.hero-title{position:absolute;right:40px;top:200px;text-align:right;line-height:1.05}
.hero-title .l1{font-size:27px;color:var(--white)}
.hero-title .l2{font-size:27px;color:var(--red)}
.hero-title .l2 span{color:var(--white)}

/* service boxes */
.services{position:absolute;top:352px;left:0;width:653px;display:flex;gap:8px;padding:0 22px}
.service{flex:1;background:rgba(20,20,20,.88);color:#ccc;display:flex;gap:8px;padding:0 8px 8px 0}
.service h3{width:100%;font-size:11px;color:var(--white);padding:6px 8px 4px}
.service .thumb{width:76px;height:52px;flex:none;margin-left:8px;background:linear-gradient(150deg,#8a97a4,#3b4651)}
.service p{font-size:7px}

/* welcome */
.welcome{display:flex;gap:18px;padding:32px 0 0;height:334px}
.welcome-main{flex:1}
.intro{display:flex;gap:12px}
.intro .photo{width:92px;height:84px;flex:none;background:linear-gradient(160deg,#aebccb,#5d6b57)}
.intro h2{font-size:15px;color:var(--ink)}
.intro h4{font-size:9px;color:var(--ink);font-weight:500;margin-bottom:4px}
.intro h4 span{color:var(--red)}
.intro p,.lead{font-size:7.5px;color:var(--muted)}
.lead{margin:8px 0 12px}
.features{display:grid;grid-template-columns:repeat(3,1fr);row-gap:12px;column-gap:8px}
.features li{list-style:none;display:flex;align-items:center;gap:6px;font-size:8.5px}
.features svg{flex:none}

.jobs{width:178px;border-left:1px solid var(--line);padding-left:12px}
.jobs h3{font-size:11px;display:flex;align-items:center;gap:5px;margin-bottom:4px}
.jobs p{font-size:7px;color:var(--muted);margin-bottom:8px}
.field{height:17px;border:1px solid var(--line);margin-bottom:6px;font-size:7px;color:#aaa;padding:3px 5px}
.field.area{height:56px}
.submit{display:block;margin-left:auto;width:70px;height:18px;background:var(--red);color:var(--white);font-size:7.5px;font-weight:700;text-align:center;line-height:18px}

/* feature band */
.band{background:var(--grey-band);height:186px;padding-top:18px}
.band .wrap{display:flex;gap:20px}
.col{flex:1}
.col-top{display:flex;gap:10px;align-items:center}
.col .thumb{width:86px;height:60px;flex:none;background:linear-gradient(160deg,#d7d7d7,#9a9a9a)}
.col .thumb.dark{background:linear-gradient(160deg,#b08f55,#3e2c1a)}
.col h3{font-size:14px;color:var(--ink);line-height:1.1}
.col p{font-size:7px;color:var(--muted);margin:8px 0}
.more{display:inline-block;background:var(--red);color:var(--white);font-size:7px;font-weight:700;padding:4px 9px}

/* footer */
.site-footer{position:absolute;top:975px;left:0;width:713px;height:205px;background:var(--footer);color:#bbb;padding-top:18px}
.site-footer .wrap{display:flex;gap:20px}
.f-col h4{font-size:10px;color:var(--white);margin-bottom:10px}
.f-col p,.f-col li{font-size:7px;list-style:none;line-height:1.9}
.addr{width:170px}
.info{width:120px}
.news{width:150px}
.socials{display:flex;gap:6px;margin-top:8px}
.socials i{width:11px;height:11px;border-radius:50%;background:#555;display:block}
.badges{margin-left:auto;display:flex;flex-direction:column;gap:10px;align-items:flex-end}
.badge-a{width:82px;height:22px;background:var(--red)}
.badge-b{width:62px;height:62px;border-radius:50%;background:#ddd}
.bottom{position:absolute;top:1180px;left:0;width:713px;height:20px;background:var(--footer-bottom);color:#888;font-size:6.5px;text-align:center;line-height:20px}
</style>
</head>
<body>
<div class="wrap">
  <header class="site-header">
    <div class="brand"><span class="dot"></span>SpanRidge Structures</div>
    <div class="call"><small>CALL US</small><strong>555 010 4821</strong></div>
  </header>
  <nav class="nav">
    <a class="active">Home</a><a>About Us</a><a>Monopole Reinforcements</a><a>Tower Reinforcements</a><a>Fabrication</a><a>Install Services</a><a>Contact Us</a>
  </nav>
  <section class="hero" role="img" aria-label="Photo of technicians climbing a lattice communication tower against the sky">
    <span class="arrow left"><svg width="8" height="12"><path d="M7 1 2 6l5 5" stroke="#fff" stroke-width="2" fill="none"/></svg></span>
    <span class="arrow right"><svg width="8" height="12"><path d="M1 1l5 5-5 5" stroke="#fff" stroke-width="2" fill="none"/></svg></span>
    <div class="hero-title"><div class="l1">Towering above the rest</div><div class="l2">Reinforcing <span>for the future</span></div></div>
  </section>
  <div class="services">
    <div class="service" style="flex-wrap:wrap">
      <h3>Monopole Reinforcements</h3>
      <div style="display:flex;gap:8px">
        <div class="thumb" role="img" aria-label="Photo of a reinforced monopole tower"></div>
        <p>SpanRidge Structures has been manufacturing monopoles and towers since 1996. This experience gives us a unique perspective for designing and building reinforcements.</p>
      </div>
    </div>
    <div class="service" style="flex-wrap:wrap">
      <h3>Tower Reinforcements</h3>
      <div style="display:flex;gap:8px">
        <div class="thumb" role="img" aria-label="Photo of a worker on a lattice tower"></div>
        <p>SpanRidge Structures has been manufacturing monopoles and towers since 1996. This experience gives us a unique perspective for designing and building reinforcements.</p>
      </div>
    </div>
  </div>

  <section class="welcome">
    <div class="welcome-main">
      <div class="intro">
        <div class="photo" role="img" aria-label="Photo of tower crew working on antennas"></div>
        <div>
          <h2>Welcome to our site</h2>
          <h4>SpanRidge Structures, Inc.<br><span>Towering above the rest</span></h4>
          <p>SpanRidge Structures, Inc. is an experienced and innovative provider of communication towers, tower reinforcements and related support. Specializing in the manufacturing, installation and maintenance of communication infrastructure products, we are regarded as pioneers.</p>
        </div>
      </div>
      <p class="lead">We invite you to explore our website, then contact us so that we may begin to develop and implement the superior, cost-effective and timely solutions that your individual project requires.</p>
      <ul class="features">
        <li><svg width="11" height="11"><circle cx="5.5" cy="5.5" r="5" fill="var(--red)"/></svg>Tower Reinforcements</li>
        <li><svg width="11" height="11"><circle cx="5.5" cy="5.5" r="5" fill="var(--red)"/></svg>Monopole Reinforcements</li>
        <li><svg width="11" height="11"><circle cx="5.5" cy="5.5" r="5" fill="var(--red)"/></svg>Antenna Support Structures</li>
        <li><svg width="11" height="11"><circle cx="5.5" cy="5.5" r="5" fill="var(--red)"/></svg>Rapid Deployment Site</li>
        <li><svg width="11" height="11"><circle cx="5.5" cy="5.5" r="5" fill="var(--red)"/></svg>Tower Accessories</li>
        <li><svg width="11" height="11"><circle cx="5.5" cy="5.5" r="5" fill="var(--red)"/></svg>Construction Services</li>
        <li><svg width="11" height="11"><circle cx="5.5" cy="5.5" r="5" fill="var(--red)"/></svg>Towers</li>
        <li><svg width="11" height="11"><circle cx="5.5" cy="5.5" r="5" fill="var(--red)"/></svg>Custom Steel Fabrication</li>
        <li><svg width="11" height="11"><circle cx="5.5" cy="5.5" r="5" fill="var(--red)"/></svg>Other Services</li>
      </ul>
    </div>
    <aside class="jobs">
      <h3><svg width="10" height="10"><rect width="10" height="10" fill="var(--red)"/></svg>Employment Opportunities</h3>
      <p>Please answer all questions. Resumes are not a substitute for a completed application.</p>
      <div class="field">Enter name</div>
      <div class="field">Enter email</div>
      <div class="field">Phone</div>
      <div class="field">Select Job Category</div>
      <div class="field area">Text</div>
      <span class="submit">SUBMIT FORM</span>
    </aside>
  </section>
</div>

<section class="band">
  <div class="wrap">
    <div class="col">
      <div class="col-top"><div class="thumb" role="img" aria-label="Technical reinforcement drawing"></div><h3>Reinforcement<br>Drawings</h3></div>
      <p>SpanRidge Structures, Inc. is an experienced provider of communication towers and tower reinforcements, specializing in manufacturing and installation.</p>
      <span class="more">READ MORE</span>
    </div>
    <div class="col">
      <div class="col-top"><div class="thumb" role="img" aria-label="Reinforcement solution diagram"></div><h3>Reinforcement<br>Solutions</h3></div>
      <p>SpanRidge Structures, Inc. is an experienced provider of communication towers and tower reinforcements, specializing in manufacturing and installation.</p>
      <span class="more">READ MORE</span>
    </div>
    <div class="col">
      <div class="col-top"><div class="thumb dark" role="img" aria-label="Photo of crew at a tower site at sunset"></div><h3>What we offer</h3></div>
      <p>SpanRidge Structures, Inc. is an experienced provider of communication towers and tower reinforcements, specializing in manufacturing and installation.</p>
      <span class="more">READ MORE</span>
    </div>
  </div>
</section>

<footer class="site-footer">
  <div class="wrap">
    <div class="f-col addr">
      <h4>Company Address</h4>
      <p>240 Harbor Mill Road<br>Bayline, Florida 32500<br>Telephone: +1 555 010 4821<br>FAX: +1 555 010 4822<br>E-mail: info@spanridge.example</p>
      <div class="socials"><i></i><i></i><i></i><i></i><i></i><i></i></div>
    </div>
    <div class="f-col info">
      <h4>Information</h4>
      <ul><li>Home</li><li>About Us</li><li>Monopole Reinforcements</li><li>Tower Reinforcements</li><li>Fabrication</li><li>Install Services</li><li>Contact Us</li></ul>
    </div>
    <div class="f-col news">
      <h4>Recent News</h4>
      <p>New crew training program opens this spring, apply online now.<br>June 12, 2015</p>
      <p>Monopole upgrade finished ahead of schedule in the Caribbean.<br>May 28, 2015</p>
    </div>
    <div class="badges">
      <div class="badge-a" role="img" aria-label="Partner badge"></div>
      <div class="badge-b" role="img" aria-label="Certification badge"></div>
    </div>
  </div>
</footer>
<div class="bottom">info@spanridge.example | all rights reserved</div>
</body>
</html>
```